Promotional ads for the upcoming book, "Beneath the Copper Lantern" by KRVO Press

We would like the following ad sizes to promote the release of our new book, "Beneath the Copper Lantern", published by KRVO Press:
1) wide skyscraper (160x600)
2) large rectangle (336x200)
3) square (250x250)
4) leaderboard (728x90)
5) inline rectangle (300x250)
The ads are to be displayed on our website, https://www.krvoarchive.org/

```html
<!DOCTYPE html>
<html lang="en">
<head>
<meta charset="utf-8">
<title>Beneath the Copper Lantern – Ad Set</title>
<link rel="stylesheet" href="https://fonts.googleapis.com/css2?family=Sorts+Mill+Goudy:ital@0;1&display=swap">
<style>
  :root{
    --canvas:#fefde8;
    --oxblood:#6e0e0e;
    --ivory:#fffaf0;
    --cream-mark:#f3e3c0;
    --stage-light:#ece3d3;
    --stage-warm:#f2d5a2;
    --sepia-pale:#d4c6a8;
    --sepia-light:#b9a887;
    --sepia-mid:#8f7d60;
    --sepia-dark:#5e4f3b;
    --ink:#3a2a1a;
  }
  *{box-sizing:border-box;margin:0;padding:0}
  html,body{width:1200px;height:1000px;overflow:hidden}
  body{background:var(--canvas);position:relative;font-family:"Sorts Mill Goudy",Georgia,serif}
  .ad{position:absolute;overflow:hidden}

  /* 600x160 banner */
  .ad-banner{left:300px;top:98px;width:600px;height:160px;background:var(--oxblood)}
  .ad-banner .headline{position:absolute;left:6px;top:20px;width:300px;text-align:center;
    color:var(--ivory);font-style:italic;font-weight:400;font-size:45px;line-height:52px}
  .ad-banner .banner-photo{position:absolute;left:307px;top:0;width:586px;height:160px;width:286px;
    background:
      radial-gradient(ellipse 30% 45% at 45% 70%, var(--sepia-dark) 0%, transparent 100%),
      radial-gradient(ellipse 60% 40% at 50% 28%, var(--sepia-mid) 0%, transparent 100%),
      linear-gradient(90deg, var(--sepia-light), var(--sepia-mid) 50%, var(--sepia-light) 85%, var(--sepia-pale))}

  /* stage ads with book */
  .ad-stage{background:linear-gradient(160deg,var(--stage-light),var(--stage-warm))}
  .ad-square{left:300px;top:275px;width:250px;height:250px}
  .ad-rect{left:567px;top:275px;width:336px;height:200px}
  .ad-inline{left:450px;top:652px;width:300px;height:250px}

  .book{position:absolute;width:15.8em;height:23.7em;box-shadow:0.4em 0.5em 0.8em rgba(90,60,20,.25)}
  .ad-square .book{left:47px;top:8px;font-size:10px}
  .ad-rect .book{left:101px;top:2px;font-size:8.3px}
  .ad-inline .book{left:68px;top:6px;font-size:10.2px}
  .book .spine{position:absolute;left:0;top:0;width:1em;height:100%;background:var(--oxblood);overflow:hidden}
  .book .spine-title{position:absolute;left:0;top:5em;width:1em;writing-mode:vertical-rl;
    color:var(--cream-mark);font-style:italic;font-size:1em;line-height:1em;white-space:nowrap}
  .book .cover-photo{position:absolute;left:1em;right:0;top:0;bottom:0;
    background:
      radial-gradient(ellipse 40% 35% at 50% 42%, var(--sepia-dark) 0%, transparent 100%),
      radial-gradient(ellipse 70% 30% at 50% 22%, var(--sepia-mid) 0%, transparent 100%),
      linear-gradient(180deg, var(--sepia-pale) 0%, var(--sepia-light) 30%, var(--sepia-mid) 70%, #7d6c50 100%)}
  .book .author{position:absolute;left:1em;right:0;top:0.5em;text-align:center;
    font-size:0.7em;letter-spacing:.12em;font-variant:small-caps;color:var(--ink)}
  .book .title-band{position:absolute;left:1em;right:0;top:13.6em;height:7.6em;
    background:rgba(70,60,40,.5);text-align:center;color:var(--ivory);padding-top:0.5em}
  .book .book-title{font-style:italic;font-size:2em;line-height:1}
  .book .subtitle{margin-top:0.6em;font-size:0.52em;letter-spacing:.05em;text-transform:uppercase;line-height:1.4}

  /* 728x90 leaderboard */
  .ad-leaderboard{left:236px;top:542px;width:728px;height:90px;background:var(--oxblood)}
  .ad-leaderboard .author-name{position:absolute;left:42px;top:45px;transform:translate(-50%,-50%) rotate(-90deg);
    color:var(--cream-mark);font-size:14px;letter-spacing:.06em}
  .ad-leaderboard .headline{position:absolute;left:0;right:0;top:14px;text-align:center;
    color:var(--ivory);font-style:italic;font-weight:400;font-size:46px;line-height:60px;
    text-shadow:0 0 3px rgba(255,200,200,.4)}
  .ad-leaderboard .publisher{position:absolute;right:26px;top:45px;display:flex;align-items:center;gap:10px;transform:translateY(-50%)}
  .ad-leaderboard .publisher-dot{width:14px;height:14px;border-radius:50%;background:var(--cream-mark)}
  .ad-leaderboard .publisher-name{writing-mode:vertical-rl;color:var(--cream-mark);font-size:14px;letter-spacing:.06em}
</style>
</head>
<body>

<section class="ad ad-banner">
  <h1 class="headline">Beneath the<br>Copper Lantern</h1>
  <div class="banner-photo" role="img" aria-label="Sepia archival group photograph from the frontier era"></div>
</section>

<section class="ad ad-stage ad-square">
  <div class="book">
    <div class="spine"><span class="spine-title">Beneath the Copper Lantern</span></div>
    <div class="cover-photo" role="img" aria-label="Sepia archival group photograph on the book cover"></div>
    <p class="author">Harold J. Wren</p>
    <div class="title-band">
      <p class="book-title">Beneath the<br>Copper Lantern</p>
      <p class="subtitle">Civilian hands of the frontier posts on<br>the river country, 1850–1890</p>
    </div>
  </div>
</section>

<section class="ad ad-stage ad-rect">
  <div class="book">
    <div class="spine"><span class="spine-title">Beneath the Copper Lantern</span></div>
    <div class="cover-photo" role="img" aria-label="Sepia archival group photograph on the book cover"></div>
    <p class="author">Harold J. Wren</p>
    <div class="title-band">
      <p class="book-title">Beneath the<br>Copper Lantern</p>
      <p class="subtitle">Civilian hands of the frontier posts on<br>the river country, 1850–1890</p>
    </div>
  </div>
</section>

<section class="ad ad-leaderboard">
  <span class="author-name">WREN</span>
  <h2 class="headline">Beneath the Copper Lantern</h2>
  <div class="publisher">
    <span class="publisher-dot"></span>
    <span class="publisher-name">KRVO</span>
  </div>
</section>

<section class="ad ad-stage ad-inline">
  <div class="book">
    <div class="spine"><span class="spine-title">Beneath the Copper Lantern</span></div>
    <div class="cover-photo" role="img" aria-label="Sepia archival group photograph on the book cover"></div>
    <p class="author">Harold J. Wren</p>
    <div class="title-band">
      <p class="book-title">Beneath the<br>Copper Lantern</p>
      <p class="subtitle">Civilian hands of the frontier posts on<br>the river country, 1850–1890</p>
    </div>
  </div>
</section>

</body>
</html>
```